BANNER FOR ONLINE CABINET COMPANY MAIN PAGE

Need 3 different banners for the main page. We are online platform for ordering cabinets, parts etc. online.
Website: trimfit.ca
A place where the banner will be placed: https://view.snapvault.example/qR7TpWzKmB4eX
Banner size: 1344x399 pixels
****Clients should get the main point that they can order everything online through the website.

Industry/Entity Type

online cabinets and parts ordering

Requirements
Must have
• online ordering icons, iphone, laptop, desktop pc - so clients get an idea that this is web based service to order cabinets

```html
<!DOCTYPE html>
<html lang="en">
<head>
<meta charset="utf-8">
<title>TrimFit – Main Page Banners</title>
<link rel="stylesheet" href="https://fonts.googleapis.com/css2?family=Oswald:wght@500;600&family=Poppins:wght@400;500&display=swap">
<style>
  :root {
    --page: #2a2a2a;
    --white: #ffffff;
    --off-white: #f8f8f8;
    --soft-grey: #ededed;
    --red: #f14346;
    --pink: #fbb4b4;
    --ink: #2b2b2b;
    --dot: #3a3a3a;
    --wood-light: #c6b6a2;
    --wood-mid: #9c8670;
    --wood-dark: #6e5c4b;
    --cool-light: #e6e7e8;
    --cool-mid: #c9cbcd;
  }
  * { margin: 0; padding: 0; box-sizing: border-box; }
  html, body { width: 1200px; height: 1126px; overflow: hidden; background: var(--page); }

  .banner {
    position: absolute; left: 60px; width: 1080px; height: 320px;
    background: var(--white); overflow: hidden;
  }
  .banner--kitchen { top: 44px; }
  .banner--shaker { top: 398px; }
  .banner--melamine { top: 750px; }
  .banner svg.shapes { position: absolute; inset: 0; width: 100%; height: 100%; }

  .copy { position: absolute; color: var(--ink); }
  .copy--centered { text-align: center; transform: translateX(-50%); }
  .copy--centered .cta-row { justify-content: center; }

  .brand {
    font-family: "Oswald", sans-serif; font-weight: 500; font-size: 38px;
    line-height: 1; color: var(--ink); letter-spacing: 0.5px;
  }
  .headline {
    font-family: "Oswald", sans-serif; font-weight: 600; font-size: 46px;
    line-height: 1; color: var(--red); margin-top: 22px; white-space: nowrap; letter-spacing: 0.3px;
  }
  .tagline {
    font-family: "Poppins", sans-serif; font-size: 16px; line-height: 1.3; color: var(--ink);
    margin-top: 10px; white-space: nowrap;
  }
  .tagline strong { font-weight: 500; color: var(--red); }

  .cta-row { display: flex; align-items: center; gap: 18px; margin-top: 18px; }
  .order-btn {
    display: inline-flex; align-items: center; justify-content: center; gap: 10px;
    width: 192px; height: 47px; flex: none;
    border: 1px solid var(--red); border-radius: 24px; background: transparent;
    font-family: "Oswald", sans-serif; font-weight: 500; font-size: 20px;
    color: var(--ink); letter-spacing: 0.5px; text-decoration: none;
  }
  .order-btn svg { width: 20px; height: 18px; }

  .devices { display: flex; align-items: flex-end; gap: 10px; }
  .devices svg { display: block; fill: none; stroke: var(--ink); stroke-width: 1.8; stroke-linejoin: round; stroke-linecap: round; }
  .device--phone { width: 16px; height: 28px; }
  .device--laptop { width: 38px; height: 26px; }
  .device--desktop { width: 34px; height: 32px; }

  .dots { position: absolute; background-image: radial-gradient(circle, var(--dot) 1.4px, transparent 1.8px); background-size: 19px 19px; }
  .dots--on-red { background-image: radial-gradient(circle, var(--ink) 1.4px, transparent 1.8px); }
</style>
</head>
<body>

<!-- Banner 1: Kitchen Cabinets -->
<section class="banner banner--kitchen">
  <svg class="shapes" viewBox="0 0 1080 320">
    <defs>
      <linearGradient id="kitchenPhoto" x1="0" y1="0" x2="1" y2="1">
        <stop offset="0" stop-color="#bfb2a3"/>
        <stop offset="0.45" stop-color="var(--wood-mid)"/>
        <stop offset="1" stop-color="#d8d3cc"/>
      </linearGradient>
    </defs>
    <rect width="1080" height="320" fill="var(--off-white)"/>
    <path d="M565,0 C660,40 700,120 625,165 C545,215 390,215 300,320 L1080,320 L1080,0 Z" fill="var(--red)"/>
    <path role="img" aria-label="Photo of a modern kitchen with wood-grain cabinets, island and mosaic backsplash" d="M600,0 C690,40 710,125 640,170 C560,220 460,240 420,320 L1080,320 L1080,0 Z" fill="url(#kitchenPhoto)"/>
    <path d="M580,0 C690,50 700,150 590,200 C500,240 430,280 420,320" fill="none" stroke="var(--red)" stroke-width="1.2"/>
  </svg>
  <div class="dots" style="left:6px;top:6px;width:28px;height:150px"></div>
  <div class="dots" style="left:398px;top:2px;width:245px;height:40px"></div>
  <div class="dots" style="left:36px;top:282px;width:300px;height:38px"></div>
  <div class="dots" style="left:1034px;top:200px;width:40px;height:120px"></div>
  <div class="copy" style="left:46px;top:42px">
    <div class="brand">TrimFit</div>
    <h2 class="headline">KITCHEN CABINETS</h2>
    <p class="tagline">Order Custom Cabinets Online at <strong>trimfit.ca</strong></p>
    <div class="cta-row">
      <a class="order-btn" href="#">
        <svg viewBox="0 0 20 18"><path d="M1 6h18l-2 10H3z M6 6l4-5 4 5" fill="none" stroke="var(--red)" stroke-width="2" stroke-linejoin="round"/><path d="M7 9v5M10 9v5M13 9v5" stroke="var(--red)" stroke-width="1.6"/></svg>
        ORDER NOW
      </a>
      <div class="devices" role="img" aria-label="Order from phone, laptop or desktop">
        <svg class="device--phone" viewBox="0 0 16 28"><rect x="1.5" y="1.5" width="13" height="25" rx="2.5"/><path d="M6.5 22.5h3"/></svg>
        <svg class="device--laptop" viewBox="0 0 38 26"><rect x="6" y="2" width="26" height="17" rx="1.5"/><path d="M1.5 23.5h35l-3-4.5h-29z"/></svg>
        <svg class="device--desktop" viewBox="0 0 34 32"><rect x="1.5" y="1.5" width="31" height="21" rx="1.5"/><path d="M13 23v5M21 23v5M9 30.5h16"/></svg>
      </div>
    </div>
  </div>
</section>

<!-- Banner 2: MDF Shaker Doors -->
<section class="banner banner--shaker">
  <svg class="shapes" viewBox="0 0 1080 320">
    <defs>
      <linearGradient id="shakerPhoto" x1="0" y1="0" x2="1" y2="1">
        <stop offset="0" stop-color="var(--cool-light)"/>
        <stop offset="0.5" stop-color="#d6d7d8"/>
        <stop offset="1" stop-color="var(--cool-mid)"/>
      </linearGradient>
    </defs>
    <rect x="0" y="0" width="200" height="320" fill="var(--red)"/>
    <ellipse cx="868" cy="60" rx="338" ry="218" fill="var(--soft-grey)"/>
    <ellipse cx="866" cy="80" rx="330" ry="226" fill="none" stroke="var(--ink)" stroke-width="1.2"/>
    <rect role="img" aria-label="Photo of white shaker-style base cabinets with countertop, sink and wine fridge" x="19" y="26" width="600" height="270" fill="url(#shakerPhoto)"/>
  </svg>
  <div class="dots dots--on-red" style="left:6px;top:0;width:20px;height:170px"></div>
  <div class="dots" style="left:140px;top:280px;width:280px;height:40px"></div>
  <div class="dots" style="left:625px;top:226px;width:70px;height:94px"></div>
  <div class="dots" style="left:930px;top:16px;width:150px;height:40px"></div>
  <div class="dots" style="left:960px;top:276px;width:120px;height:40px"></div>
  <div class="copy copy--centered" style="left:845px;top:34px">
    <div class="brand">TrimFit</div>
    <h2 class="headline">MDF SHAKER DOORS</h2>
    <p class="tagline">Order Custom Doors Online at <strong>trimfit.ca</strong></p>
    <div class="cta-row">
      <a class="order-btn" href="#">
        <svg viewBox="0 0 20 18"><path d="M1 6h18l-2 10H3z M6 6l4-5 4 5" fill="none" stroke="var(--red)" stroke-width="2" stroke-linejoin="round"/><path d="M7 9v5M10 9v5M13 9v5" stroke="var(--red)" stroke-width="1.6"/></svg>
        ORDER NOW
      </a>
      <div class="devices" role="img" aria-label="Order from phone, laptop or desktop">
        <svg class="device--phone" viewBox="0 0 16 28"><rect x="1.5" y="1.5" width="13" height="25" rx="2.5"/><path d="M6.5 22.5h3"/></svg>
        <svg class="device--laptop" viewBox="0 0 38 26"><rect x="6" y="2" width="26" height="17" rx="1.5"/><path d="M1.5 23.5h35l-3-4.5h-29z"/></svg>
        <svg class="device--desktop" viewBox="0 0 34 32"><rect x="1.5" y="1.5" width="31" height="21" rx="1.5"/><path d="M13 23v5M21 23v5M9 30.5h16"/></svg>
      </div>
    </div>
  </div>
</section>

<!-- Banner 3: Textured Melamine -->
<section class="banner banner--melamine">
  <svg class="shapes" viewBox="0 0 1080 320">
    <defs>
      <linearGradient id="melaminePhoto" x1="0" y1="0" x2="1" y2="1">
        <stop offset="0" stop-color="#d9d8d4"/>
        <stop offset="0.5" stop-color="var(--wood-light)"/>
        <stop offset="1" stop-color="var(--wood-dark)"/>
      </linearGradient>
    </defs>
    <ellipse role="img" aria-label="Photo of a textured wood-grain melamine desk counter with a bar stool" cx="860" cy="340" rx="520" ry="320" fill="url(#melaminePhoto)"/>
    <path d="M400,320 C520,120 760,0 940,20 C1000,26 1050,50 1080,80" fill="none" stroke="var(--red)" stroke-width="1.2"/>
    <circle cx="270" cy="38" r="248" fill="var(--pink)"/>
    <circle cx="262" cy="62" r="254" fill="none" stroke="var(--ink)" stroke-width="1.2"/>
  </svg>
  <div class="dots" style="left:362px;top:16px;width:300px;height:40px"></div>
  <div class="dots" style="left:10px;top:150px;width:40px;height:170px"></div>
  <div class="dots" style="left:1034px;top:8px;width:40px;height:200px"></div>
  <div class="copy copy--centered" style="left:270px;top:34px">
    <div class="brand">TrimFit</div>
    <h2 class="headline">TEXTURED MELAMINE</h2>
    <p class="tagline">Order Custom Panels Online at <strong>trimfit.ca</strong></p>
    <div class="cta-row">
      <a class="order-btn" href="#">
        <svg viewBox="0 0 20 18"><path d="M1 6h18l-2 10H3z M6 6l4-5 4 5" fill="none" stroke="var(--red)" stroke-width="2" stroke-linejoin="round"/><path d="M7 9v5M10 9v5M13 9v5" stroke="var(--red)" stroke-width="1.6"/></svg>
        ORDER NOW
      </a>
      <div class="devices" role="img" aria-label="Order from phone, laptop or desktop">
        <svg class="device--phone" viewBox="0 0 16 28"><rect x="1.5" y="1.5" width="13" height="25" rx="2.5"/><path d="M6.5 22.5h3"/></svg>
        <svg class="device--laptop" viewBox="0 0 38 26"><rect x="6" y="2" width="26" height="17" rx="1.5"/><path d="M1.5 23.5h35l-3-4.5h-29z"/></svg>
        <svg class="device--desktop" viewBox="0 0 34 32"><rect x="1.5" y="1.5" width="31" height="21" rx="1.5"/><path d="M13 23v5M21 23v5M9 30.5h16"/></svg>
      </div>
    </div>
  </div>
</section>

</body>
</html>
```